Velbrant Insurance Solutions Drop Off Flyer

We need a clean, powerful, one page flyer to drop off at businesses. it needs to simple yet needs to jump out for a decision maker to read...

Target Market(s)

Business owners with over 50 employees.....all types of industries...

Industry/Entity Type

Insurance

Font styles to use
Serif
Sans Serif

Colors
0355a3
3176b5
85acd3
ffffff

Requirements
Must have
• You must include all wording on the PDF i included titled Velbrant Flyer Idea. Of course, the color and layout is up to you but the wording needs to be included.
Nice to have
• Just a one page Letter size drop off

```html
<!DOCTYPE html>
<html lang="en">
<head>
<meta charset="utf-8">
<title>Velbrant Insurance Solutions – Drop Off Flyer</title>
<link href="https://fonts.googleapis.com/css2?family=Montserrat:wght@400;500;600;700&display=swap" rel="stylesheet">
<style>
  :root{
    --brand-deep:#0355a3;
    --brand-mid:#3176b5;
    --brand-soft:#85acd3;
    --paper:#ffffff;
    --ink:#1d1d1f;
    --ink-soft:#333840;
    --photo-dark:#1b2a40;
    --photo-light:#3e5675;
    --rim:#c9ccd1;
  }
  *{box-sizing:border-box;margin:0;padding:0}
  html,body{width:854px;height:1200px;overflow:hidden;background:#fff}
  body{font-family:"Montserrat",Arial,sans-serif;color:var(--ink)}
  .flyer{position:relative;width:854px;height:1200px;background:var(--paper);overflow:hidden}

  .hero-band{position:absolute;left:0;top:0;width:854px;height:362px;background:var(--brand-deep)}
  .hero-globe{position:absolute;left:0;top:0;width:854px;height:460px}

  .brand{position:absolute;top:452px;left:0;width:854px;display:flex;justify-content:center;align-items:center;gap:12px}
  .brand-dot{width:38px;height:38px;border-radius:50%;background:var(--brand-deep)}
  .brand-name{font-weight:700;font-size:28px;color:var(--ink-soft);letter-spacing:.5px;line-height:1}
  .brand-sub{display:block;font-size:10.5px;font-weight:700;letter-spacing:1px;margin-top:3px}

  .headline{position:absolute;top:524px;width:854px;text-align:center}
  .headline-kicker{font-size:25px;font-weight:500;color:var(--ink);letter-spacing:.5px}
  .headline-main{font-size:37px;font-weight:700;color:var(--brand-deep);letter-spacing:.5px;line-height:1.15}

  .offer{position:absolute;top:616px;left:0;width:854px;height:174px;background:var(--brand-mid);color:var(--paper);text-align:center;padding-top:8px}
  .offer-ask{font-size:19px;font-weight:500;letter-spacing:1px}
  .offer-figure{font-size:42px;font-weight:600;line-height:1.05}
  .offer-detail{font-size:17px;font-weight:500;letter-spacing:.3px}
  .offer-detail strong{font-weight:700}
  .offer-close{font-size:50px;font-weight:600;line-height:1.15;letter-spacing:.5px}

  .points{position:absolute;top:806px;width:854px;display:flex;flex-direction:column;align-items:center;gap:14px}
  .point{display:flex;flex-direction:column;align-items:center}
  .tick{width:16px;height:16px;margin-bottom:2px}
  .point-lead{font-size:18px;font-weight:500;margin-bottom:-11px;background:var(--paper);padding:0 8px;position:relative;z-index:1}
  .point-box{border:2px solid var(--brand-soft);padding:12px 24px 6px;font-size:21px;font-weight:500}

  .contact{position:absolute;top:992px;left:0;width:854px;height:150px}
  .contact-card{position:absolute;left:40px;top:4px;width:360px;text-align:center;font-size:14.5px;line-height:1.42;text-transform:uppercase;letter-spacing:.3px;font-style:normal}
  .contact-divider{position:absolute;left:424px;top:0;width:2px;height:138px;background:var(--ink)}
  .cta{position:absolute;left:450px;top:0;width:364px;text-align:center}
  .cta-label{display:inline-block;background:var(--brand-deep);color:var(--paper);font-size:27px;font-weight:500;padding:2px 18px;letter-spacing:.5px}
  .cta-line{font-size:27px;font-weight:500;line-height:1.1;margin-top:4px}
  .cta-line + .cta-line{margin-top:0}
  .cta-phone{font-size:40px;font-weight:500;margin-top:6px}

  .footer-rule{position:absolute;top:1147px;left:0;width:854px;height:4px;background:var(--brand-deep)}
  .footer{position:absolute;top:1156px;left:0;width:854px;height:44px;background:var(--brand-deep);color:var(--paper);text-align:center;font-size:26px;font-weight:600;line-height:44px;letter-spacing:2px}
</style>
</head>
<body>
<main class="flyer">
  <div class="hero-band"></div>
  <svg class="hero-globe" viewBox="0 0 854 460">
    <defs>
      <linearGradient id="photoTone" x1="0" y1="0" x2="1" y2="1">
        <stop offset="0" stop-color="var(--photo-light)"/>
        <stop offset=".55" stop-color="var(--photo-dark)"/>
        <stop offset="1" stop-color="#2a3e5a"/>
      </linearGradient>
      <clipPath id="globeClip"><ellipse cx="427" cy="180" rx="362" ry="258"/></clipPath>
      <clipPath id="rimSides"><rect x="0" y="300" width="250" height="160"/><rect x="604" y="300" width="250" height="160"/></clipPath>
    </defs>
    <ellipse cx="427" cy="180" rx="370" ry="266" fill="#ffffff"/>
    <g clip-path="url(#globeClip)">
      <rect x="0" y="0" width="854" height="460" fill="url(#photoTone)" role="img" aria-label="Photo of a businessman's hands sheltering glowing insurance icons: plane, family, medical kit and car"/>
      <g fill="none" stroke="#ffffff" stroke-width="7">
        <line x1="427" y1="0" x2="427" y2="460"/>
        <ellipse cx="427" cy="180" rx="190" ry="300"/>
        <line x1="0" y1="200" x2="854" y2="200"/>
        <path d="M40 30 Q427 85 814 30"/>
        <path d="M70 370 Q427 315 784 370"/>
      </g>
    </g>
    <ellipse cx="427" cy="180" rx="380" ry="276" fill="none" stroke="var(--rim)" stroke-width="4" clip-path="url(#rimSides)"/>
  </svg>

  <div class="brand">
    <span class="brand-dot"></span>
    <span class="brand-name">VELBRANT<span class="brand-sub">INSURANCE SOLUTIONS</span></span>
  </div>

  <header class="headline">
    <p class="headline-kicker">READ ONLY IF YOU CARE ABOUT</p>
    <h1 class="headline-main">YOUR BUSINESS’ BOTTOM LINE</h1>
  </header>

  <section class="offer">
    <p class="offer-ask">HOW WOULD YOU LIKE TO PAY</p>
    <p class="offer-figure">18% LESS</p>
    <p class="offer-detail">ON YOUR <strong>NEXT WORKERS COMPENSATION</strong> RENEWAL, AT</p>
    <p class="offer-close">NO COST TO YOU?</p>
  </section>

  <section class="points">
    <div class="point">
      <svg class="tick" viewBox="0 0 16 16"><rect x="1" y="1" width="14" height="14" fill="none" stroke="var(--brand-mid)" stroke-width="1.5"/><path d="M4 8l3 3 5-6" fill="none" stroke="var(--brand-mid)" stroke-width="2"/></svg>
      <span class="point-lead">You Don’t Even Need To Change</span>
      <span class="point-box">Your Current Broker or Insurance Company</span>
    </div>
    <div class="point">
      <svg class="tick" viewBox="0 0 16 16"><rect x="1" y="1" width="14" height="14" fill="none" stroke="var(--brand-mid)" stroke-width="1.5"/><path d="M4 8l3 3 5-6" fill="none" stroke="var(--brand-mid)" stroke-width="2"/></svg>
      <span class="point-lead">We Are Not Brokers Or Agents.</span>
      <span class="point-box">We Are Licensed Workers Compensation Cost Reduction Specialists</span>
    </div>
  </section>

  <section class="contact">
    <address class="contact-card">
      Marla Quenby<br>
      Velbrant Insurance Solutions<br>
      Office: 555-014-2290<br>
      Cell: 555-017-3846 | Fax: 555-019-5521<br>
      4810 Harlow Crest<br>
      Brookhaven, CA 90000<br>
      License# 0K48273
    </address>
    <div class="contact-divider"></div>
    <div class="cta">
      <span class="cta-label">CALL US TODAY</span>
      <p class="cta-line">FOR A 5 MINUTE</p>
      <p class="cta-line">OVERVIEW</p>
      <p class="cta-phone">555-017-3846</p>
    </div>
  </section>

  <div class="footer-rule"></div>
  <footer class="footer">www.velbrant.net</footer>
</main>
</body>
</html>
```